International Health Supplement Company Needs Packaging and Label Redesign

Copper Lantern LLC requires a redesign for 1 internationally sold product and accompanying designs for 5 additional products. The additional products are currently sold locally and yet to be released internationally.

Our company is honest, premium, and passionate about supplements. We adopt a 'no BS' stance and as such source only the finest ingredients and deliver high-quality liquid health supplements to customers globally. We do not compromise on quality and do not apologise for price.

We want a clean, crisp design that conveys ‘premium, cutting-edge, boutique’ at a glance. We feel our current design appeals more to the 'chest beaters' rather than the 'chess players' that our research has indicated are our customers.

We have SIX PRODUCTS TOTAL in our range and feel individual color cues to distinguish the different products would greatly assist customer navigation i.e. Customers will identify ‘red’ means ‘product X’ without reading the label. (Examples attached and below we believe do this well).

Current 30ml bottle, cap, and dropper are in black and will remain so. Current label is black, however, we have a white label on our local product (example attached) and prefer the look of it.

Packaging is currently black and could remain so however most products that appeal to our target market are in white with color accents.

One consideration we have is that the product up until now has been selling exceptionally well so we need to retain some kind of familiarity with the existing branding. Perhaps that’s just the logo.

Logo can be revised i.e. add company name and/or company slogan.

Products are: (Function - Name)

Testosterone Support - Tongkat Ali (current)
Hormone Support - Jiaogulan
Energy Support - Ashwaghanda
Libido Support - Krachai Dam (for men)
Libido Support - Kacip Fatimah (for women)
Sleep Support - Wild Chamomile

Packaging: 4.6cm (L) x 8.0cm (W) x 11.2cm (H)
Label: 30 mL bottle

https://www.folioweb.example/gallery/TONIC-BOX-STUDY-2011/7402518
http://www.pelkastudio.example/projects/#/river-tea/
https://www.folioweb.example/gallery/31420786/Velmora-Skin
https://au.pinboardly.example/pin/592719083317915736/
https://au.pinboardly.example/pin/36916877689752218/
http://velto.example/en/portfolio/logo-redesign/

Target Market(s)

Generation X Men (and their partners), 36-55, upper middle class, who appreciate quality products.

Industry/Entity Type

Health Product

Font styles to use
Serif
Sans Serif

Requirements
Must have
• Packaging - Principal Display Panel (Front):
• 1. Function & Name of each product i.e 'Testosterone Support' & 'Tongkat Ali'
• 2. '30ml' AND '1 fl oz' (text size 1.8in / 3.2mm / 9 point min.)
• 3. 'Dietary Supplement'
• Packaging - Information Panel (Right):
• 1. Supplement Facts Panel (template accepted for drafts)
• 2. Directions: (lorum ipsum accepted for drafts)
• 3. Safety Warning: (lorum ipsum accepted for drafts)
• 4. 'Manufactured for: Copper Lantern LLC'
• 5. 'Alder Bay, Northland'
• 6. '(555) 014 2200'
• 7. 'Product of Thailand'
• Bottle Label:
• 3. 'Dietary Supplement'
• 4. Supplement Facts Panel (template accepted for drafts)
• 5. Directions: (lorum ipsum accepted for drafts)
• 6. Safety Warning: (forum ipsum accepted for drafts)
• 7. 'Manufactured for: Copper Lantern LLC'
• 8. 'Alder Bay, Northland'
• 9. '(555) 014 2200'
• 10. 'Product of Thailand'
Nice to have
• Updated logo with company name 'Copper Lantern' and/or company slogan 'Quality Without Compromise' added.
Should not have
• No photos or stock images.
• No elements of the current design (excluding logo) to remain i.e. 'Otter Finn', 'Testosterone Booster', 'Increase Lean Muscle', 'Stabilise Hormones', 'Boost Endurance', 'Improve Muscle Naturally', are all to be omitted.

```html
<!DOCTYPE html>
<html lang="en">
<head>
<meta charset="utf-8">
<title>Ashwaghanda Energy Support – Carton Dieline</title>
<link href="https://fonts.googleapis.com/css2?family=Roboto:wght@300;400;700&family=Roboto+Condensed:wght@300;400;700&family=Comfortaa:wght@500&display=swap" rel="stylesheet">
<style>
  :root {
    --brand-red: #ec1a4b;
    --brand-deep: #b10d36;
    --ink: #231f20;
    --line: #4a4a4a;
    --paper: #ffffff;
    --maker-gold: #e9c23a;
  }
  * { margin: 0; padding: 0; box-sizing: border-box; }
  html, body { width: 1200px; height: 987px; overflow: hidden; background: var(--paper); }
  .carton { position: relative; width: 1200px; height: 987px; font-family: "Roboto", sans-serif; color: var(--ink); }
  .dieline, .print-shapes { position: absolute; left: 0; top: 0; }
  .abs { position: absolute; }

  .brand-mark { display: flex; align-items: center; gap: 8px; }
  .brand-mark .dot { width: 26px; height: 26px; border-radius: 50%; background: var(--brand-red); }
  .brand-mark .name { font-family: "Roboto Condensed", sans-serif; font-weight: 700; font-size: 17px; color: var(--brand-red); letter-spacing: .5px; }

  .product-name { font-weight: 300; font-size: 39px; letter-spacing: -.5px; white-space: nowrap; transform: translateX(-50%); }
  .product-name .accent { color: var(--brand-red); }
  .slogan { font-family: "Roboto Condensed", sans-serif; font-weight: 300; font-size: 12px; transform: translateX(-50%); white-space: nowrap; }
  .function { font-family: "Roboto Condensed", sans-serif; font-weight: 300; color: #fff; font-size: 34px; line-height: 35px; }
  .volume { font-family: "Roboto Condensed", sans-serif; font-weight: 300; font-size: 15px; white-space: nowrap; }
  .volume .bar { padding: 0 4px; }
  .dietary { font-family: "Roboto Condensed", sans-serif; font-weight: 300; font-size: 12.5px; letter-spacing: -.3px; white-space: nowrap; }
  .supply { font-family: "Roboto Condensed", sans-serif; line-height: 1; }
  .supply .top { font-size: 12px; }
  .supply .top b { color: var(--brand-red); font-weight: 700; }
  .supply .sub { display: block; background: var(--ink); color: #fff; font-size: 5px; letter-spacing: 3.4px; text-align: center; padding: 1px 0; margin-top: 1px; }

  .info { font-family: "Roboto Condensed", sans-serif; font-weight: 700; font-size: 9px; }
  .facts-box, .warning-box { border: 1px solid var(--line); padding: 3px; background: #fff; }
  .facts-box .inner, .warning-box .inner { border: 1.5px solid var(--brand-red); height: 100%; padding: 4px 5px; }
  .facts-title { font-family: "Roboto Condensed", sans-serif; font-weight: 700; font-size: 14px; border-bottom: 2px solid var(--ink); padding-bottom: 2px; }
  .facts-head { display: flex; justify-content: space-between; font-family: "Roboto Condensed", sans-serif; font-size: 6px; border-bottom: 1px solid var(--ink); padding: 2px 0 1px; }
  .facts-rule { border-bottom: 2px solid var(--ink); margin-top: 26px; }
  .warning-box .inner { font-family: "Roboto Condensed", sans-serif; font-weight: 700; font-size: 8.4px; line-height: 12px; }

  .band-slogan { font-family: "Roboto Condensed", sans-serif; color: #fff; font-size: 16px; white-space: nowrap; }
  .website { font-family: "Comfortaa", sans-serif; font-weight: 500; font-size: 12.5px; white-space: nowrap; }
  .maker { font-family: "Roboto Condensed", sans-serif; color: var(--maker-gold); font-size: 5.5px; line-height: 7px; white-space: nowrap; }
  .maker .co { font-size: 9px; line-height: 11px; }
  .origin { font-family: "Roboto Condensed", sans-serif; color: #fff; font-size: 7.5px; white-space: nowrap; }

  .pattern-grey { background: radial-gradient(ellipse at center, #ececec 0%, #f7f7f7 60%, transparent 75%); }
  .pattern-red { background: radial-gradient(ellipse at center, rgba(255,255,255,.12) 0%, rgba(255,255,255,0) 70%); }
</style>
</head>
<body>
<div class="carton">

  <svg class="print-shapes" width="1200" height="987" viewBox="0 0 1200 987">
    <rect x="0" y="238" width="1200" height="21" fill="var(--brand-red)"/>
    <rect x="0" y="542" width="377" height="12" fill="var(--brand-deep)"/>
    <rect x="0" y="554" width="377" height="102" fill="var(--brand-red)"/>
    <path d="M656 554 L660 536 Q662 528 672 528 L1200 528 L1200 554 Z" fill="var(--brand-deep)"/>
    <path d="M568 736 L590 600 Q598 554 650 554 L1200 554 L1200 656 L660 656 Z" fill="var(--brand-red)"/>
    <path d="M568 736 L582 656 L700 656 L680 720 L672 736 Z" fill="var(--brand-deep)"/>
    <path d="M0 666 L264 666 Q272 666 275 672 L280 690 L377 690" fill="none" stroke="#999" stroke-width=".8"/>
    <path d="M700 666 L780 666 Q786 666 790 674 L800 690 L808 690 Q814 690 818 680 L822 666 L1200 666" fill="none" stroke="#999" stroke-width=".8"/>
  </svg>

  <svg class="dieline" width="1200" height="987" viewBox="0 0 1200 987" fill="none" stroke="var(--line)" stroke-width=".8">
    <rect x="30" y="250" width="347" height="486"/>
    <path d="M30 736 L30 936 L37 978 Q38 986 46 986 L368 986 Q376 986 377 978 L377 736"/>
    <path d="M377 250 L577 250 M377 736 L577 736 M377 250 L377 736"/>
    <path d="M377 250 L377 222 L388 208 L388 118 Q388 112 394 112 L562 112 Q568 112 568 118 L568 208 L577 222"/>
    <path d="M377 736 L388 872 Q388 874 394 874 L560 874 Q566 874 566 868 L566 770 L577 756"/>
    <rect x="577" y="50" width="348" height="686"/>
    <path d="M577 50 L582 8 Q584 0 592 0 L908 0 Q916 0 918 8 L925 50"/>
    <path d="M925 250 L1124 250 L1124 736 L925 736"/>
    <path d="M925 222 L934 208 L934 118 Q934 112 940 112 L1106 112 Q1112 112 1112 118 L1112 208 L1124 222 L1124 250"/>
    <path d="M925 756 L934 770 L936 868 Q936 874 942 874 L1106 874 Q1112 874 1112 868 L1124 736"/>
    <path d="M1124 250 L1168 250 L1168 736 L1124 736"/>
  </svg>

  <!-- left front panel -->
  <div class="abs brand-mark" style="left:136px;top:397px;">
    <span class="dot"></span><span class="name">Copper Lantern</span>
  </div>
  <div class="abs product-name" style="left:204px;top:466px;">ASHWA<span class="accent">GHANDA</span></div>
  <div class="abs slogan" style="left:204px;top:522px;">QUALITY WITHOUT COMPROMISE</div>
  <div class="abs pattern-red" role="img" aria-label="Hexagonal molecule pattern in tonal red" style="left:0;top:556px;width:170px;height:92px;"></div>
  <div class="abs function" style="left:210px;top:570px;">ENERGY<br>SUPPORT</div>
  <div class="abs volume" style="left:56px;top:670px;">30ml <span class="bar">|</span>1 fl oz</div>
  <div class="abs dietary" style="left:171px;top:668px;">DIETARY SUPPLEMENT</div>
  <div class="abs supply" style="left:293px;top:666px;"><span class="top"><b>ONE</b>MONTH</span><span class="sub">SUPPLY</span></div>

  <!-- information side panel -->
  <div class="abs info" style="left:391px;top:282px;">Direction : Shake well before use.</div>
  <div class="abs facts-box" style="left:392px;top:364px;width:170px;height:92px;">
    <div class="inner">
      <div class="facts-title">Supplement Facts</div>
      <div class="facts-head"><span>Amount Per Serving</span><span>% Daily Value</span></div>
      <div class="facts-rule"></div>
    </div>
  </div>
  <div class="abs pattern-grey" role="img" aria-label="Grey hexagonal molecule diagram" style="left:392px;top:462px;width:108px;height:134px;"></div>
  <div class="abs warning-box" style="left:392px;top:613px;width:170px;height:84px;">
    <div class="inner">
      SAFETY WARNING :<br>Do not use if seal is broken<br>Keep out reach of children<br>Keep away from open fame<br><span style="display:block;margin-top:6px;">STORAGE : Story in cool &amp; dry place.</span>
    </div>
  </div>

  <!-- top lid -->
  <div class="abs brand-mark" style="left:682px;top:144px;">
    <span class="dot"></span><span class="name">Copper Lantern</span>
  </div>

  <!-- main front panel -->
  <div class="abs brand-mark" style="left:682px;top:331px;">
    <span class="dot"></span><span class="name">Copper Lantern</span>
  </div>
  <div class="abs product-name" style="left:752px;top:416px;font-size:43px;">ASHWA<span class="accent">GHANDA</span></div>
  <div class="abs band-slogan" style="left:690px;top:532px;">QUALITY WITHOUT COMPROMISE</div>
  <div class="abs function" style="left:661px;top:570px;">ENERGY<br>SUPPORT</div>
  <div class="abs pattern-red" role="img" aria-label="Hexagonal molecule pattern in tonal red" style="left:800px;top:560px;width:192px;height:88px;"></div>
  <div class="abs volume" style="left:593px;top:674px;color:#fff;">30ml <span class="bar">|</span>1 fl oz</div>
  <div class="abs supply" style="left:720px;top:666px;"><span class="top"><b>ONE</b>MONTH</span><span class="sub">SUPPLY</span></div>
  <div class="abs dietary" style="left:826px;top:670px;">DIETARY SUPPLEMENT</div>

  <!-- right side panel -->
  <div class="abs pattern-grey" role="img" aria-label="Grey hexagonal molecule diagram" style="left:968px;top:284px;width:152px;height:188px;"></div>
  <div class="abs maker" style="left:1016px;top:588px;">Manufactured for :<br><span class="co">Copper Lantern LLC</span><br>Alder Bay, Northland<br>(555) 014 2200</div>
  <div class="abs origin" style="left:1016px;top:636px;">PRODUCT OF THAILAND</div>
  <div class="abs website" style="left:947px;top:672px;">www.copperlantern.example</div>

</div>
</body>
</html>
```